Innovative Freezer Label Design

Create a versatile and innovative freezer label design with universal appeal, suitable for different functionalities. The design should cater to a diverse audience, including those who freeze meals for meal prepping, batch cooking, and the restaurant industry. Our vision is a visually striking and distinctive design that embodies simplicity.

Example "our current labels feature essential details like "Contents" and "Date." We recognize these as crucial points of information. Currently, the challenge lies in creating various labels for different marketplaces, considering language barriers. A proposed solution involves the integration of universal icons to replace specific words, promoting practicality for international sales."

Kindly note that design concepts should not be restricted to our current product, brand guideline, logo, or the provided example.

Our goal is not only product differentiation but also increased sales through a blend of functionality and aesthetics.

The following are examples of freezer labels designs. Kindly do not restrict your designs to the examples. The designs must be universal (for language barrier purposes)

Examples:
https://www.snaprovel.co.uk/pin/5820174630298837415/
https://www.snaprovel.co.uk/pin/5820174630298837419/
https://www.snaprovel.co.uk/pin/5820174630298837408/
https://www.snaprovel.co.uk/pin/5820174630298837322/
https://www.snaprovel.co.uk/pin/5820174630298898764/

Please reach out if you have any questions.

Thank you

```html
<!DOCTYPE html>
<html lang="en">
<head>
<meta charset="UTF-8">
<title>Freezer Label – Content &amp; Date</title>
<link rel="stylesheet" href="https://fonts.googleapis.com/css2?family=Poppins:wght@600&display=swap">
<style>
  :root {
    --stage-light: #f4f4f4;
    --stage-dark: #e2e2e2;
    --frame-teal: #1f4f57;
    --frame-teal-soft: #2b5f66;
    --panel-white: #ffffff;
    --label-sage: #8fad9f;
    --icon-ink: #1f4f57;
  }
  * { box-sizing: border-box; margin: 0; padding: 0; }
  html, body {
    width: 1018px;
    height: 1200px;
    overflow: hidden;
  }
  body {
    background: radial-gradient(ellipse at 50% 40%, var(--stage-light) 0%, var(--stage-dark) 100%);
    font-family: "Poppins", sans-serif;
    position: relative;
  }
  .freezer-label {
    position: absolute;
    left: 59px;
    top: 374px;
    width: 900px;
    height: 451px;
    box-shadow: 0 10px 24px rgba(0, 0, 0, 0.18);
  }
  .label-frame {
    position: absolute;
    inset: 0;
    background: linear-gradient(135deg, var(--frame-teal) 0%, var(--frame-teal-soft) 50%, var(--frame-teal) 100%);
  }
  .label-panel {
    position: absolute;
    left: 40px;
    top: 42px;
    right: 39px;
    bottom: 42px;
    background: var(--panel-white);
  }
  .field-icon {
    position: absolute;
    color: var(--icon-ink);
  }
  .content-icon { left: 32px; top: 22px; width: 62px; height: 80px; }
  .date-icon { left: 43px; top: 294px; width: 48px; height: 48px; }
  .field-title {
    position: absolute;
    color: var(--label-sage);
    font-weight: 600;
    line-height: 1;
  }
  .content-title { left: 113px; top: 40px; font-size: 46px; }
  .date-title { left: 118px; top: 306px; font-size: 28px; }
  .date-slash {
    position: absolute;
    top: 298px;
    color: var(--label-sage);
    font-size: 38px;
    font-weight: 600;
    line-height: 1;
  }
  .slash-one { left: 326px; }
  .slash-two { left: 497px; }
</style>
</head>
<body>
  <div class="freezer-label">
    <div class="label-frame" role="img" aria-label="Dark teal border with a faint line pattern of vegetables, fruit and dishes"></div>
    <div class="label-panel">
      <svg class="field-icon content-icon" viewBox="0 0 62 80" fill="none" stroke="currentColor" stroke-width="3" stroke-linejoin="round" stroke-linecap="round" aria-hidden="true">
        <rect x="14" y="8" width="40" height="52" rx="3"/>
        <rect x="26" y="3" width="16" height="9" rx="2"/>
        <line x1="21" y1="22" x2="34" y2="22"/>
        <line x1="21" y1="30" x2="32" y2="30"/>
        <line x1="21" y1="38" x2="30" y2="38"/>
        <path d="M42 24 l6 18 l-9 -4 z"/>
        <path d="M6 50 l20 20 l6 -6 l-20 -20 z"/>
        <path d="M26 70 l8 2 l-2 -8"/>
      </svg>
      <div class="field-title content-title">Content:</div>

      <svg class="field-icon date-icon" viewBox="0 0 48 48" fill="none" stroke="currentColor" stroke-width="3" stroke-linejoin="round" aria-hidden="true">
        <rect x="3" y="7" width="42" height="38" rx="3"/>
        <line x1="3" y1="16" x2="45" y2="16"/>
        <line x1="14" y1="3" x2="14" y2="10"/>
        <line x1="34" y1="3" x2="34" y2="10"/>
        <g fill="currentColor" stroke="none">
          <rect x="10" y="22" width="4" height="4"/><rect x="18" y="22" width="4" height="4"/><rect x="26" y="22" width="4" height="4"/><rect x="34" y="22" width="4" height="4"/>
          <rect x="10" y="29" width="4" height="4"/><rect x="18" y="29" width="4" height="4"/><rect x="26" y="29" width="4" height="4"/><rect x="34" y="29" width="4" height="4"/>
          <rect x="10" y="36" width="4" height="4"/><rect x="18" y="36" width="4" height="4"/><rect x="26" y="36" width="4" height="4"/><rect x="34" y="36" width="4" height="4"/>
        </g>
      </svg>
      <div class="field-title date-title">Date:</div>
      <span class="date-slash slash-one">/</span>
      <span class="date-slash slash-two">/</span>
    </div>
  </div>
</body>
</html>
```